INNOVATIVE DESIGN NEEDED FOR FINANCIAL COMPANY

INTERNATIONAL FIRM IN HONG KONG NEEDS A MODERN BUSINESS CARD DESIGN. ONE SIDE ENGLISH OTHER SIDE IN CHINESE. WE ARE OPEN TO CHANGING FONTS AND COLOR. SHOULD BE A CARD THAT IS PROFESSIONAL DEALING WITH HIGH NET WORTH CLIENTELE. BOTH SIDES OF THE CARD WILL BE THE SAME, HOWEVER, THE WORDING ON ONE SIDE WILL BE ENGLISH AND THE OTHER SIDE IN CHINESE (CAN ASSIST IN THE LETTERING - CAN PROVIDE ONCE CARD DESIGN IS ACCEPTED.

Target Market(s)

Hong Kong/CHINA

Contact Information for Business Card

ATTRACTIVE MODERN

```html
<!DOCTYPE html>
<html lang="en">
<head>
<meta charset="utf-8">
<title>Larchmere Asset Management – Business Card</title>
<link rel="stylesheet" href="https://fonts.googleapis.com/css2?family=Roboto+Condensed:wght@400;700&family=Noto+Sans+TC:wght@400;700&family=Saira+Semi+Condensed:wght@400;500&display=swap">
<style>
  :root {
    --stage: #bdbdbd;
    --green: #13835e;
    --green-soft: #2a9472;
    --paper: #f2f2f2;
    --paper-shade: #e4e4e4;
    --ink: #2b2b2b;
    --ghost: #dcdcdc;
    --white: #ffffff;
  }
  * { margin: 0; padding: 0; box-sizing: border-box; }
  html, body { width: 1200px; height: 576px; overflow: hidden; }
  body { background: var(--stage); position: relative; }

  .card {
    position: absolute;
    top: 139px;
    width: 484px;
    height: 292px;
    border-radius: 14px;
    overflow: hidden;
  }
  .card--front { left: 82px; background: var(--green); color: var(--white); }
  .card--back { left: 602px; background: linear-gradient(135deg, var(--paper) 0%, var(--paper-shade) 100%); color: var(--ink); }

  .decor-circle { position: absolute; border-radius: 50%; }
  .card--front .decor-circle { left: 250px; top: -10px; width: 290px; height: 290px; background: var(--green-soft); opacity: .55; }
  .card--back .decor-circle { left: 268px; top: -10px; width: 280px; height: 280px; background: var(--ghost); opacity: .8; }

  .brand { position: absolute; display: flex; align-items: center; }
  .brand__dot { border-radius: 50%; flex: none; }
  .brand__names { display: flex; flex-direction: column; }
  .brand__zh { font-family: "Noto Sans TC", sans-serif; font-weight: 700; line-height: 1.15; letter-spacing: .5px; }
  .brand__en { font-family: "Roboto Condensed", sans-serif; font-weight: 700; line-height: 1.2; }

  .card--front .brand { left: 90px; top: 111px; }
  .card--front .brand__dot { width: 66px; height: 66px; background: var(--white); margin-right: 26px; }
  .card--front .brand__zh { font-size: 21px; }
  .card--front .brand__en { font-size: 16.5px; }

  .front-web {
    position: absolute; left: 0; right: 0; top: 249px; text-align: center;
    font-family: "Saira Semi Condensed", sans-serif; font-size: 11.5px;
  }

  .card--back .brand { left: 14px; top: 30px; }
  .card--back .brand__dot { width: 54px; height: 54px; background: var(--green); margin-right: 8px; }
  .card--back .brand__zh { font-size: 18px; color: var(--ink); }
  .card--back .brand__en { font-size: 13.5px; color: var(--ink); }

  .name-marker { position: absolute; left: -24px; top: 132px; width: 38px; height: 38px; border-radius: 50%; background: var(--green); }

  .person { position: absolute; left: 23px; top: 131px; }
  .person__name { font-family: "Roboto Condensed", "Noto Sans TC", sans-serif; font-weight: 700; font-size: 17px; color: var(--green); }
  .person__name .zh { font-family: "Noto Sans TC", sans-serif; }
  .person__title { font-family: "Saira Semi Condensed", "Noto Sans TC", sans-serif; font-size: 11.5px; margin-top: 1px; }

  .contact { position: absolute; left: 26px; top: 184px; list-style: none; font-family: "Saira Semi Condensed", sans-serif; font-size: 11.5px; }
  .contact li { display: flex; align-items: center; height: 16.5px; }
  .contact svg { width: 10px; height: 10px; margin-right: 7px; fill: var(--green); }

  .address { position: absolute; left: 23px; top: 236px; font-family: "Saira Semi Condensed", "Noto Sans TC", sans-serif; font-size: 11.5px; line-height: 17px; }
</style>
</head>
<body>

<section class="card card--front">
  <div class="decor-circle"></div>
  <div class="brand">
    <div class="brand__dot"></div>
    <div class="brand__names">
      <span class="brand__zh">朗松資產管理有限公司</span>
      <span class="brand__en">Larchmere Asset Management Ltd</span>
    </div>
  </div>
  <p class="front-web">www.larchmereassets.com</p>
</section>

<section class="card card--back">
  <div class="decor-circle"></div>
  <div class="brand">
    <div class="brand__dot"></div>
    <div class="brand__names">
      <span class="brand__zh">朗松資產管理有限公司</span>
      <span class="brand__en">Larchmere Asset Management Ltd</span>
    </div>
  </div>

  <div class="name-marker"></div>
  <div class="person">
    <p class="person__name">CHAN Michael <span class="zh">陳明輝</span></p>
    <p class="person__title">Responsible Officer / 负责人员</p>
  </div>

  <ul class="contact">
    <li><svg viewBox="0 0 10 10"><path d="M1 3.2C1 2 2.5 1.2 5 1.2S9 2 9 3.2V4H7V3.2H3V4H1z M2.2 5 3.4 4h3.2l1.2 1v3.6H2.2z"/></svg>828-555-0142</li>
    <li><svg viewBox="0 0 10 10"><path d="M0.5 2h9v6h-9z M1 2.5 5 5.5 9 2.5" stroke="#fff" stroke-width=".8"/></svg>chanmichael@larchmereassets.com</li>
    <li><svg viewBox="0 0 10 10"><circle cx="5" cy="5" r="4.5"/><path d="M0.5 5h9 M5 0.5c-2.4 2.5-2.4 6.5 0 9 M5 0.5c2.4 2.5 2.4 6.5 0 9" stroke="#fff" stroke-width=".7" fill="none"/></svg>www.larchmereassets.com</li>
  </ul>

  <div class="address">
    <p>58 Harbour Rd., Any City, Hong Kong 123456</p>
    <p>58 海港道, 任何城市, 香港 123456</p>
  </div>
</section>

</body>
</html>
```